Website Design for a DJ Entertainment and Productions Comany

We are a full service DJ Entertainment and Productions company looking to have a strong presence in our local market and need a phenomenal website design to drive clients to the site but then also keep them there. We cater to all types of different events varying from weddings to proms to corporate events, birthdays, bar mitzvah's and so on and so on. We also do full lighting for any type of event and we also offer a photobooth service for various events. The best way to get an idea of the services that we offer is to visit http://www.velvarmusicworks.com/index.html This site is NOT our own but only linked as an example of what we do and will give you an overall overview of what we offer.
We are looking for pure creativity as there are multiple facets to our company and the services we offer. On the one hand we can provide a night club party atmosphere for Proms or dances but on the other hand we also provide professional full service emcee/DJ for weddings and formal events. The key for this site would be to have the pages for each category match the look and feel of the actual service provided, ie the Wedding page will look more refined and professional vs the Party DJ page. Each page needs to fit the overall feel of the Company and Logo though. Here is a list of pages that we would need to have on the final site.
HOME PAGE
PROFESSINAL DJS- This will have info. and pricing of our DJ services for everything but weddings. Should have pics and videos somewhere on this page.
WEDDINGS- All wedding package pricing and info. This page should look more elegant, formal and high class compared to the other pages.
PHOTOBOOTH-Page with info, pricing on photobooth see http://www.glimmerboxkiosk.com/
LIGHTING DESIGN-Info on our lighting services along with pricing
CORPORATE EVENTS-Info on services and pricing for corporate events. This page should seem more professional centered towards business clientele.
CLIENT LOGIN-Page for existing clients to logon to update info and fill out information.
CONNECT WITH US- Social Media links.
Our logo was submitted through Pixel Forum but I am open to suggestions on revisions if you feel the need to change it. Color is also not set in stone.
Updates
I have increased my budget $200 more. Please submit your designs for review, deadline is approaching quickly. Also see brief for revisions.
Thank you.
Target Market(s)
Broad Range but usually Under 40
Industry/Entity Type
Night Club
Look and feel

```html
<!DOCTYPE html>
<html lang="en">
<head>
<meta charset="utf-8">
<title>NOVA Entertainment &amp; Productions</title>
<link href="https://fonts.googleapis.com/css2?family=Arimo:wght@400;700&family=Roboto+Condensed:wght@400;700&display=swap" rel="stylesheet">
<style>
:root{
  --red:#d8101a;
  --red-dark:#7a0a0c;
  --maroon:#4a0a08;
  --gold:#f2c21b;
  --orange:#e88a12;
  --ink:#1d1d2c;
  --panel:#1f1f1f;
  --white:#ffffff;
  --footer:#2a2a2a;
}
*{margin:0;padding:0;box-sizing:border-box}
html,body{width:1064px;height:1200px;overflow:hidden;background:#fff;font-family:Arimo,Arial,sans-serif}
.page{position:relative;width:1064px;height:1200px;overflow:hidden}
.hero-bg{position:absolute;left:0;top:0;width:1064px;height:522px;
  background:
   radial-gradient(ellipse 420px 300px at 1000px 420px,#ffe600 0%,rgba(255,200,0,.6) 40%,transparent 75%),
   radial-gradient(ellipse 500px 380px at 760px 260px,#e0141a 0%,rgba(200,20,40,.5) 50%,transparent 80%),
   linear-gradient(100deg,#1a1e78 0%,#2f2fa0 35%,#5a1a8a 60%,#b0142a 80%,#f0a010 100%);}
.hero-fade{position:absolute;left:0;top:470px;width:1064px;height:52px;background:linear-gradient(#ffffff00,#ffffffcc)}
.abs{position:absolute}
.login{left:648px;top:0;width:355px;height:37px;background:linear-gradient(#a5080c,#6a0406);border-radius:0 0 10px 10px;display:flex;align-items:center;gap:6px;padding:0 6px}
.login .field{width:134px;height:24px;border-radius:12px;background:#fff;font-size:12px;color:#888;padding:5px 11px}
.login .go{width:56px;height:26px;border-radius:13px;background:linear-gradient(#ff2a2a,#b00008);color:#fff;font-weight:700;font-size:13px;text-align:center;line-height:26px;margin-left:6px}
.brand{left:72px;top:26px;display:flex;align-items:center;gap:12px;color:var(--red);font-weight:700}
.brand .mark{width:78px;height:78px;border-radius:50%;background:var(--red)}
.brand .name{font-size:52px;line-height:48px;letter-spacing:1px}
.brand .sub{font-size:11px;line-height:14px;display:block;letter-spacing:.2px}
.tagline{left:397px;top:62px;font-family:"Roboto Condensed",Arial,sans-serif;font-size:19px;line-height:24px;color:#fff;letter-spacing:.5px}
.tagline span{display:block;color:var(--gold);font-weight:700;text-align:right}
.call{left:777px;top:57px;width:226px;height:55px;border-radius:8px;background:linear-gradient(#ff2a2a,#a0060a);border:1px solid #ff6a6a;display:flex;align-items:center;padding-left:12px;gap:12px;color:#fff}
.call .lab{font-size:12px;font-weight:700;display:block}
.call .num{font-size:23px;font-weight:700;display:block;line-height:24px}
.nav{left:43px;top:130px;width:960px;height:42px;border-radius:8px;background:linear-gradient(#8a0a0c,#4a0406);display:flex;align-items:center;justify-content:space-between;padding:0 24px 0 18px}
.nav a{color:#fff;text-decoration:none;font-size:13px;font-weight:700;line-height:42px}
.nav a.active{background:var(--red);padding:0 12px;height:48px;line-height:52px;margin-top:-6px}
.slider{left:47px;top:195px;width:949px;height:305px;border-radius:16px;background:linear-gradient(#f5b020,var(--orange) 60%,#c46a08);box-shadow:0 2px 6px #0006}
.slide-photo{left:63px;top:212px;width:921px;height:234px;background:linear-gradient(90deg,#3a2a6a,#6a5aa0 30%,#c8a4b4 55%,#4a4aa0 80%,#2a2a6a)}
.dots{left:838px;top:396px;display:flex;gap:20px}
.dots i{width:10px;height:10px;border-radius:50%;background:#ff5a5a}
.dots i:first-child{background:#a0060a}
.caption{left:63px;top:446px;width:921px;height:38px;background:linear-gradient(#f4f4f4,#cfcfcf);display:flex;align-items:center;justify-content:space-between;padding:0 10px 0 15px;font-weight:700;font-size:15px;color:#111}
.btn-more{background:linear-gradient(#c8341a,#8a1a08);color:#fff;font-weight:400;font-size:15px;padding:5px 19px;border:1px solid #e86a4a}
.welcome{left:31px;top:538px;width:667px}
.welcome h1{color:var(--red);font-size:20px;font-weight:700;margin-bottom:17px}
.welcome p{font-size:12.4px;line-height:16px;color:#222;text-align:justify;margin-bottom:14px}
.welcome p.gap{margin-top:30px}
.read-more{left:613px;top:819px;color:var(--red-dark);font-weight:700;font-size:13px;text-decoration:underline}
.events{left:733px;top:541px;width:279px;height:297px;background:var(--panel);padding:14px 19px}
.events h2{color:#fff;font-family:"Roboto Condensed",Arial,sans-serif;font-size:17px;font-weight:700;margin-bottom:13px}
.event{display:flex;gap:10px;height:87px;position:relative}
.event .thumb{width:82px;height:66px;border:1px solid var(--orange);background:linear-gradient(135deg,#2a2a7a,#b48ab0 50%,#3a2a5a)}
.event p{color:#fff;font-size:12.5px;line-height:16px;width:158px}
.event .more{position:absolute;right:0;top:47px;color:#f2b84a;font-weight:700;font-size:13px}
.services{left:31px;top:850px;width:981px;height:210px;background:linear-gradient(#5a0e0a,var(--maroon))}
.services .pie{left:12px;top:12px}
.services h2{left:70px;top:18px;font-family:"Roboto Condensed",Arial,sans-serif;font-size:24px;font-weight:700;color:var(--gold)}
.services .note{right:13px;top:25px;color:#fff;font-size:13px;font-weight:700}
.cards{left:12px;top:61px;display:flex;gap:12px}
.card{width:182px;height:138px;border-radius:5px;background:#c9c9c9;border:3px solid #d8d8d8;position:relative;overflow:hidden}
.card .ph{height:72px}
.card .label{position:absolute;left:0;right:0;top:80px;text-align:center;font-family:"Roboto Condensed",Arial,sans-serif;font-weight:700;font-size:19px}
.card .click{position:absolute;left:0;right:0;top:108px;text-align:center;font-size:12.5px;color:#111}
.card{background:linear-gradient(#ffffff,#d4d4d4)}
.footer{left:0;top:1076px;width:1064px;height:60px;background:linear-gradient(#3a3a3a,#1e1e1e)}
.footer .links{left:44px;top:22px;color:#fff;font-size:13px;word-spacing:2px}
.footer .connect{left:774px;top:22px;color:#fff;font-size:13px;font-weight:700}
.footer .social{left:904px;top:16px;display:flex;gap:14px}
.footer .social i{width:22px;height:22px;border-radius:50%;background:#e8e8e8}
.copy{left:0;top:1136px;width:1064px;height:64px;background:#000;color:#fff;font-size:13px;text-align:center;padding-top:15px}
</style>
</head>
<body>
<div class="page">
  <div class="hero-bg"></div>
  <div class="hero-fade abs"></div>

  <form class="login abs"><div class="field">User Name</div><div class="field">Password</div><div class="go">GO</div></form>

  <div class="brand abs"><span class="mark"></span><div><span class="name">NOVA</span><span class="sub">ENTERTAINMENT &amp; PRODUCTIONS</span></div></div>

  <div class="tagline abs">PROFESSIONAL DJ'S FOR ALL YOUR<span>SPECIAL OCCASION...</span></div>

  <div class="call abs">
    <svg width="28" height="38" viewBox="0 0 28 38" aria-hidden="true"><path d="M6 3c3-2 6 0 7 3l1 5c0 2-2 3-4 4 1 5 3 9 7 12 2-1 3-3 5-2l4 3c2 2 1 5-2 7-4 3-11 0-16-8S1 7 6 3z" fill="#fff"/></svg>
    <div><span class="lab">Call Us :</span><span class="num">01632 960 417</span></div>
  </div>

  <nav class="nav abs">
    <a href="#">PROFESSIONAL DJS</a><a href="#" class="active">WEDDINGS</a><a href="#">PHOTOBOOTH</a><a href="#">LIGHTING DESIGN</a><a href="#">CORPORATE EVENTS</a><a href="#">CLIENT LOGIN</a><a href="#">CONNECT WITH US</a>
  </nav>

  <div class="slider abs"></div>
  <div class="slide-photo abs" role="img" aria-label="Photo of a crowd dancing and singing at a lively party"></div>
  <div class="dots abs"><i></i><i></i><i></i><i></i><i></i></div>
  <div class="caption abs"><span>Lorem ipsum dolor sit amet, consectetur adipiscing elit. Aliquam tincidunt mi id libero egestas ut</span><span class="btn-more">READ MORE...</span></div>

  <section class="welcome abs">
    <h1>WELCOME TO NOVA ENTERTAINMENT &amp; PRODUCTIONS</h1>
    <p>Lorem ipsum dolor sit amet, consectetur adipiscing elit. Aliquam tincidunt mi id libero egestas ut interdum nibh cursus. Nulla erat orci, adipiscing vel molestie ac, vehicula in dui. Proin vel lorem in tellus placerat eleifend. Duis iaculis lorem a ipsum euismod vel ullamcorper arcu placerat. Aenean elementum tortor vel nisi bibendum bibendum. Aliquam fringilla feugiat a</p>
    <p>Lorem ipsum dolor sit amet, consectetur adipiscing elit. Aliquam tincidunt mi id libero egestas ut interdum nibh cursus. Nulla erat orci, gilla. Lorem ipsum dolor sit amet, consectetur adipiscing elit. Aliquam tincidunt mi id libero egestas ut interdum nibh cursus. Nulla erat orci, gilla.</p>
    <p class="gap">Lorem ipsum dolor sit amet, consectetur adipiscing elit. Aliquam tincidunt mi id libero egestas ut interdum nibh cursus. Nulla erat orci, gilla. Lorem ipsum dolor sit amet, consectetur adipiscing elit. Aliquam tincidunt mi id libero egestas ut interdum nibh cursus. Nulla erat orci, gilla.</p>
  </section>
  <a class="read-more abs">Read More &gt;</a>

  <aside class="events abs">
    <h2>OUR LETEST EVENTS...</h2>
    <div class="event"><div class="thumb" role="img" aria-label="Photo of a singer at a party"></div><p>Lorem ipsum dolor sit amet, consectetur adipisc-ing Lorem</p><span class="more">More...</span></div>
    <div class="event"><div class="thumb" role="img" aria-label="Photo of a singer at a party"></div><p>Lorem ipsum dolor sit amet, consectetur adipisc-ing Lorem</p><span class="more">More...</span></div>
    <div class="event"><div class="thumb" role="img" aria-label="Photo of a singer at a party"></div><p>Lorem ipsum dolor sit amet, consectetur adipisc-ing Lorem</p><span class="more">More...</span></div>
  </aside>

  <section class="services abs">
    <svg class="pie abs" width="40" height="40" viewBox="0 0 40 40" aria-hidden="true"><circle cx="20" cy="20" r="19" fill="#e8a010"/><path d="M20 20V1a19 19 0 0 1 18 24z" fill="#d82a10"/><path d="M20 20L38 25A19 19 0 0 1 8 35z" fill="#f2d020"/><path d="M20 20L8 35A19 19 0 0 1 20 1z" fill="#5aa020"/></svg>
    <h2 class="abs">OUR ALL PROFESSIONAL SERVICES</h2>
    <span class="note abs">Click below our service for complete information &amp; price list</span>
    <div class="cards abs">
      <div class="card"><div class="ph" role="img" aria-label="Photo of a DJ under purple stage lights" style="background:linear-gradient(135deg,#3a2aa0,#e050c0 60%,#a0a0ff)"></div><div class="label" style="color:#1a3aa0">PROFEESIONAL DJ</div><div class="click">CLICK HERE &nbsp;DETAILS</div></div>
      <div class="card"><div class="ph" role="img" aria-label="Photo of a wedding reception table with flowers" style="background:linear-gradient(#e8dcc8,#d8c0a0 60%,#c04040)"></div><div class="label" style="color:#8a1a9a">WEDDINGS</div><div class="click">CLICK HERE &nbsp;DETAILS</div></div>
      <div class="card"><div class="ph" role="img" aria-label="Photo of friends posing in a photobooth" style="background:linear-gradient(90deg,#3a2a2a,#c08a7a 50%,#6a4a3a)"></div><div class="label" style="color:#1a7a1a">PHOTOBOOTH</div><div class="click">CLICK HERE &nbsp;DETAILS</div></div>
      <div class="card"><div class="ph" role="img" aria-label="Photo of an event hall with lighting" style="background:linear-gradient(#5a1a4a,#c04a6a 60%,#7a3a4a)"></div><div class="label" style="color:#c01a1a">LIGHTING DESIGN</div><div class="click">CLICK HERE &nbsp;DETAILS</div></div>
      <div class="card"><div class="ph" role="img" aria-label="Photo of a microphone at a corporate event" style="background:linear-gradient(90deg,#d8d8d8,#8a8a8a 50%,#e0c8a0)"></div><div class="label" style="color:#333">CORPORATE EVENTS</div><div class="click">CLICK HERE &nbsp;DETAILS</div></div>
    </div>
  </section>

  <footer class="footer abs">
    <div class="links abs">Home &nbsp;I&nbsp; Our Services &nbsp;I&nbsp; About Us &nbsp;I&nbsp; Why Nova Advant &nbsp;I&nbsp; FAQ &nbsp;I&nbsp; Reach Us &nbsp;I&nbsp; News &amp; Events &nbsp;I&nbsp; Contact</div>
    <div class="connect abs">CONNET WITH US</div>
    <div class="social abs" aria-label="Social media links"><i></i><i></i><i></i></div>
  </footer>
  <div class="copy abs">Copyright Text</div>
</div>
</body>
</html>
```